I would like a new business card designed. I am a kitchen installer for cabinet makers.
I install:
-kitchens
-vanities units
-laundry cabinets
-pantries
-wardrobe shelving
I would like the colors lime green and greys used.
servicing all areas
Also needs to include the words- residential, commercial, industrial
I also want a logo that can be used on work clothes
Modern looking
Target Market(s)
cabinet makers
Industry/Entity Type
Business
Contact Information for Business Card
RJ joinery & fitouts pty ltd
0418729564
rjjfit@mailbox-example.com.au
www.facebook.com/rjjoinery
Logo styles of interest
Emblem Logo
Look and feel

```html
<!DOCTYPE html>
<html lang="en">
<head>
<meta charset="utf-8">
<title>RJ Joinery &amp; Fitouts – Business Card</title>
<link rel="stylesheet" href="https://fonts.googleapis.com/css2?family=Questrial&family=Poiret+One&family=Montserrat:wght@700&display=swap">
<style>
  :root {
    --lime: #b5c435;
    --lime-light: #c8d45a;
    --charcoal: #2f2f30;
    --grey-mid: #5c5c5e;
    --backdrop: #e3e3e3;
    --ink-dark: #3a3a2a;
  }
  * { box-sizing: border-box; margin: 0; padding: 0; }
  html, body {
    width: 1200px; height: 1200px; overflow: hidden;
    background: radial-gradient(circle at 50% 45%, #f4f4f4, var(--backdrop));
    font-family: "Questrial", sans-serif;
  }
  .card {
    position: absolute; left: 220px; width: 760px; height: 434px;
    border-radius: 34px 34px 34px 34px;
    background: radial-gradient(ellipse at 45% 40%, var(--grey-mid) 0%, #424244 45%, var(--charcoal) 85%);
    overflow: hidden;
    box-shadow: 0 8px 22px rgba(0,0,0,.22);
  }
  .card--front { top: 84px; }
  .card--back { top: 582px; }

  /* Front */
  .stripe { position: absolute; top: 0; bottom: 0; background: var(--lime); }
  .stripe--thin { left: 648px; width: 16px; }
  .stripe--wide { left: 682px; width: 52px; }
  .stripe--wide::after {
    content: ""; position: absolute; left: 0; right: 0; top: 0; height: 45%;
    background: rgba(255,255,255,.18);
  }
  .front-brand {
    position: absolute; left: 110px; top: 178px; width: 480px; text-align: center;
  }
  .front-brand__name {
    color: var(--lime); font-size: 38px; letter-spacing: 1px; line-height: 1.2;
  }
  .front-brand__rule {
    display: block; height: 3px; background: var(--lime); margin-top: 10px;
  }

  /* Back */
  .header-mark {
    position: absolute; left: 40px; top: 24px;
    color: var(--lime); font-size: 62px; line-height: 1;
  }
  .header-band {
    position: absolute; left: 136px; right: 0; top: 38px; height: 60px;
    background: linear-gradient(180deg, var(--lime-light) 0%, var(--lime) 55%);
    display: flex; align-items: center; padding-left: 76px;
    font-family: "Poiret One", sans-serif; font-size: 34px; color: var(--ink-dark);
    font-weight: 400; letter-spacing: .5px;
  }
  .header-band .sep { margin: 0 14px; }
  .header-rule {
    position: absolute; left: 52px; right: 0; top: 108px; height: 4px; background: var(--lime);
  }
  .name-tab {
    position: absolute; left: 0; top: 194px; width: 82px; height: 24px; background: var(--lime);
  }
  .person-name {
    position: absolute; left: 88px; top: 184px;
    font-family: "Montserrat", sans-serif; font-weight: 700; font-size: 32px; color: var(--lime);
  }
  .contacts { position: absolute; left: 52px; top: 276px; list-style: none; }
  .contacts li {
    display: flex; align-items: center; gap: 12px;
    color: var(--lime); font-size: 25px; height: 44px;
  }
  .contacts svg { width: 28px; height: 28px; flex: none; }
  .contacts .square { width: 24px; height: 24px; background: var(--lime); flex: none; margin: 0 2px; }
  .divider {
    position: absolute; left: 472px; top: 178px; width: 3px; height: 232px; background: var(--lime);
  }
  .services { position: absolute; left: 494px; top: 206px; list-style: none; }
  .services li {
    color: var(--lime); font-size: 27px; height: 34px; line-height: 34px;
  }
  .services li::before { content: "• "; font-size: 22px; }
</style>
</head>
<body>
  <section class="card card--front" aria-label="Business card front">
    <div class="stripe stripe--thin"></div>
    <div class="stripe stripe--wide"></div>
    <div class="front-brand">
      <p class="front-brand__name">RJ Joinery &amp; Fitouts Pty Ltd</p>
      <span class="front-brand__rule"></span>
    </div>
  </section>

  <section class="card card--back" aria-label="Business card back">
    <div class="header-mark">RJ</div>
    <div class="header-band">Residential<span class="sep">|</span>Commercial<span class="sep">|</span>Industrial</div>
    <div class="header-rule"></div>

    <div class="name-tab"></div>
    <h1 class="person-name">Ryan Jarvis</h1>

    <ul class="contacts">
      <li>
        <svg viewBox="0 0 24 24" aria-hidden="true"><path fill="#b5c435" d="M6.6 10.8a15.1 15.1 0 0 0 6.6 6.6l2.2-2.2a1 1 0 0 1 1-.25 11.4 11.4 0 0 0 3.6.57 1 1 0 0 1 1 1V20a1 1 0 0 1-1 1A17 17 0 0 1 3 4a1 1 0 0 1 1-1h3.5a1 1 0 0 1 1 1c0 1.25.2 2.45.57 3.57a1 1 0 0 1-.25 1z"/></svg>
        0418 729 564
      </li>
      <li>
        <svg viewBox="0 0 24 24" aria-hidden="true"><rect x="2" y="5" width="20" height="14" fill="none" stroke="#b5c435" stroke-width="2"/><path d="M2 5l10 8 10-8M2 19l7-7M22 19l-7-7" fill="none" stroke="#b5c435" stroke-width="2"/></svg>
        rjjfit@mailbox-example.com.au
      </li>
      <li>
        <span class="square" aria-hidden="true"></span>
        /rjjoinery
      </li>
    </ul>

    <div class="divider"></div>
    <ul class="services">
      <li>Kitchens</li>
      <li>Vanities Units</li>
      <li>Laundry Cabinets</li>
      <li>Pantries</li>
      <li>Wardrobe Shelving</li>
    </ul>
  </section>
</body>
</html>
```